Business Card for premium dental clinic

We are a premium dental clinic based in Brasov, Romania with more than 15 year on the market, providing quality dental treatment made by a team of more specialized dentists, working with modern equipment as a solution to beautiful and healthy teeth.

Our current logo for the clinic use 2 square with colors black and gold - dr Corbescu - studio, using family fonts Bodoni, Myriad Pro and Segoe Print.
Depending on the printing we used some gold CMYK background or gold foil picture background or a gold gradient.
We want a business card:
- eye catching business card
- distinguished business card
- premium design
- to keep the color scheme of black and gold
- to attract the customers to spent time reading the information
- modern concept

```html
<!DOCTYPE html>
<html lang="en">
<head>
<meta charset="utf-8">
<title>dr Corbescu studio – business card</title>
<link href="https://fonts.googleapis.com/css2?family=Montserrat:wght@400;500;700&display=swap" rel="stylesheet">
<style>
  :root{
    --backdrop:#2f2926;
    --card-black:#151515;
    --card-white:#ffffff;
    --gold:#f2c92c;
    --ink-light:#f4f4f4;
    --ink-dark:#151515;
  }
  *{box-sizing:border-box;margin:0;padding:0}
  html,body{width:1200px;height:716px;overflow:hidden;background:var(--backdrop)}
  .canvas{position:relative;width:1200px;height:716px;font-family:"Montserrat",sans-serif}
  .card{position:absolute;top:208px;width:525px;height:300px;border-radius:6px;overflow:hidden;
        box-shadow:0 14px 30px rgba(0,0,0,.45)}
  .card--front{left:45px;background:var(--card-black)}
  .card--back{left:630px;background:var(--card-white)}

  .brand{position:absolute;display:flex;align-items:center;gap:12px;font-weight:500;letter-spacing:.5px}
  .brand__square{width:34px;height:34px;flex:none}
  .brand__name{font-size:22px;line-height:1.15;white-space:nowrap}
  .card--front .brand{left:50%;top:50%;transform:translate(-50%,-50%)}
  .card--front .brand__square{background:var(--gold)}
  .card--front .brand__name{color:var(--gold)}
  .card--back .brand{left:34px;top:122px}
  .card--back .brand__square{background:var(--ink-dark)}
  .card--back .brand__name{color:var(--ink-dark);font-size:19px}

  .divider{position:absolute;inset:0}
  .contact{position:absolute;left:290px;top:88px;color:var(--ink-light)}
  .contact__name{color:var(--gold);font-weight:700;font-size:27px;letter-spacing:1px;margin-bottom:12px}
  .contact__line{display:flex;align-items:center;gap:7px;font-size:14px;line-height:22px}
  .contact__line svg{width:11px;height:11px;flex:none}
  .contact__address{font-size:14px;line-height:22px;margin-top:4px}
</style>
</head>
<body>
<main class="canvas">
  <section class="card card--front">
    <div class="brand"><span class="brand__square"></span><span class="brand__name">dr Corbescu studio</span></div>
  </section>

  <section class="card card--back">
    <svg class="divider" viewBox="0 0 525 300" aria-hidden="true">
      <polygon points="258,0 525,0 525,300 214,300" fill="var(--card-black)"/>
      <line x1="258" y1="0" x2="214" y2="300" stroke="var(--gold)" stroke-width="3"/>
    </svg>
    <div class="brand"><span class="brand__square"></span><span class="brand__name">dr Corbescu<br>studio</span></div>
    <div class="contact">
      <h1 class="contact__name">DR CORBESCU</h1>
      <p class="contact__line">
        <svg viewBox="0 0 12 12"><path d="M2.5 1l2 2.2-1 1.3a7 7 0 0 0 4 4l1.3-1 2.2 2-1.3 1.5C5.5 11 1 6.5 1 2.3z" fill="var(--gold)"/></svg>
        +40 268 555 019</p>
      <p class="contact__line">
        <svg viewBox="0 0 12 12"><rect x="1" y="2.5" width="10" height="7" fill="none" stroke="var(--gold)" stroke-width="1.2"/><path d="M1 2.5l5 4 5-4" fill="none" stroke="var(--gold)" stroke-width="1.2"/></svg>
        info@drcorbescu.ro</p>
      <p class="contact__line">
        <svg viewBox="0 0 12 12"><circle cx="6" cy="6" r="5" fill="none" stroke="var(--gold)" stroke-width="1.1"/><ellipse cx="6" cy="6" rx="2.2" ry="5" fill="none" stroke="var(--gold)" stroke-width="1"/><line x1="1" y1="6" x2="11" y2="6" stroke="var(--gold)" stroke-width="1"/></svg>
        www.drcorbescu.ro</p>
      <p class="contact__address">Strada Lungă 48,<br>Brașov 500058, Romania</p>
    </div>
  </section>
</main>
</body>
</html>
```